Professional and creatice Life Coach - Business Card design

I just relaunched my website and now i a need a correspoonding business card for my task as life coach. My website is www.tbalrond.com as reference. The compass is kind of a symbol for my work, as I help people navigate through their challenging phases in life. The business card should be colorful, but not too playful as I also adress business people. So it sould be creative, but professional (also to suport my other business as Management Consultant)

Target Market(s)

People who want to get teir problems resolved, in business, partnership and other personal realms

Industry/Entity Type

Life Coaching

Contact Information for Business Card

Front side should include Name, Phone number, Email, Website and address

Font styles to use
Sans Serif

Colors
add136

Requirements
Must have
• "Mag. Leopold Brantner" -> Name
"Energetische Praxis" -> Jobtitle (describing my profession as life coach)
colours and style should match my website www.tbalrond.com
Nice to have
• a compass as a symbol

```html
<!DOCTYPE html>
<html lang="de">
<head>
<meta charset="utf-8">
<title>Leopold Brantner – Visitenkarte</title>
<link rel="stylesheet" href="https://fonts.googleapis.com/css2?family=Arimo:wght@400;700&family=Montserrat:wght@300&display=swap">
<style>
  :root {
    --backdrop: #2a2a2c;
    --card: #161617;
    --card-edge: #1e1e20;
    --accent: #add136;
    --white: #ffffff;
    --muted: #a6a6a6;
    --divider: #6a6a6a;
  }
  * { margin: 0; padding: 0; box-sizing: border-box; }
  html, body {
    width: 1200px; height: 900px; overflow: hidden;
    background: var(--backdrop);
  }
  .canvas {
    position: relative; width: 1200px; height: 900px;
  }
  .card {
    position: absolute; left: 320px; width: 560px; height: 330px;
    background: linear-gradient(160deg, var(--card-edge), var(--card));
    box-shadow: 0 8px 24px rgba(0,0,0,.45);
    overflow: hidden;
  }
  .card::after {
    content: ""; position: absolute; left: 0; right: 0; bottom: 0;
    height: 10px; background: var(--accent);
  }
  .card--front { top: 100px; }
  .card--back { top: 470px; }

  /* front */
  .wordmark {
    position: absolute; left: 0; right: 0; top: 128px;
    display: flex; align-items: center; justify-content: center; gap: 18px;
  }
  .wordmark__dot {
    width: 34px; height: 34px; border-radius: 50%; background: var(--accent);
  }
  .wordmark__name {
    font-family: "Montserrat", sans-serif; font-weight: 300;
    font-size: 40px; color: var(--white); letter-spacing: .5px;
  }

  /* back */
  .identity {
    position: absolute; top: 96px; left: 0; width: 100%; text-align: center;
    font-family: "Arimo", sans-serif;
  }
  .identity__name {
    font-weight: 700; font-size: 24px; color: var(--accent);
  }
  .identity__role {
    font-size: 15px; color: var(--muted); margin-top: 4px;
  }
  .details {
    position: absolute; top: 196px; left: 0; width: 100%;
    display: flex; justify-content: center;
    font-family: "Arimo", sans-serif; font-size: 15px; color: var(--muted);
  }
  .address {
    text-align: right; padding-right: 16px; line-height: 21px;
    border-right: 1px solid var(--divider); padding-top: 2px; height: 72px;
  }
  .contact {
    list-style: none; padding-left: 16px; line-height: 22px;
    color: #c9c9c9;
  }
  .contact li { display: flex; align-items: center; gap: 7px; }
  .contact svg { width: 13px; height: 13px; fill: var(--accent); flex: none; }
</style>
</head>
<body>
<main class="canvas">
  <section class="card card--front" aria-label="Vorderseite">
    <div class="wordmark">
      <span class="wordmark__dot"></span>
      <span class="wordmark__name">Leopold Brantner</span>
    </div>
  </section>

  <section class="card card--back" aria-label="Rückseite">
    <div class="identity">
      <h1 class="identity__name">Mag. Leopold Brantner</h1>
      <p class="identity__role">Energetische Praxis</p>
    </div>
    <div class="details">
      <address class="address" style="font-style:normal">
        Lindenweg 14<br>5020 Salzburg Österreich
      </address>
      <ul class="contact">
        <li>
          <svg viewBox="0 0 16 16" aria-hidden="true"><path d="M3.6 1.2l2.3 2.6-1.3 2a9 9 0 0 0 5.6 5.6l2-1.3 2.6 2.3-1.6 2.4C7.6 14.8 1.2 8.4 1.2 2.8z"/></svg>
          +43 660 4817392
        </li>
        <li>
          <svg viewBox="0 0 16 16" aria-hidden="true"><path d="M1 3h14v10H1z" fill="none"/><path d="M1 3h14L8 9z"/><path d="M1 4.5l7 6 7-6V13H1z"/></svg>
          leopold@brantner.one
        </li>
        <li>
          <svg viewBox="0 0 16 16" aria-hidden="true"><circle cx="8" cy="8" r="7"/><path d="M1 8h14M8 1c-3 3.5-3 10.5 0 14M8 1c3 3.5 3 10.5 0 14" stroke="#161617" stroke-width="1.1" fill="none"/></svg>
          www.tbalrond.com
        </li>
      </ul>
    </div>
  </section>
</main>
</body>
</html>
```